Flyer / Mailer for Business Debt Relief Business - Tillbrook Partners 6" x 11"

We need a 6" x 11" double sided flyer. This will be sent out to potential customers with high interest business loans. We would like the design to coordinate with the colors of our logo. I have included a mock up that we sketched out. I have also included a file of a mailer we received that we would like to use as a template (not colors or fonts, just set up). I have also included an .ai file of our logo.

```html
<!DOCTYPE html>
<html lang="en">
<head>
<meta charset="utf-8">
<title>Tillbrook Partners Mailer</title>
<link href="https://fonts.googleapis.com/css2?family=Bebas+Neue&family=Lato:ital,wght@0,400;0,700;1,400;1,700;1,900&display=swap" rel="stylesheet">
<style>
  :root {
    --navy: #0f4470;
    --blue: #0a7cc4;
    --green: #6cb33e;
    --green-dark: #4f9a2c;
    --ink: #1c2f4a;
    --grey-text: #444;
    --page: #e9eaec;
    --white: #ffffff;
  }
  * { margin: 0; padding: 0; box-sizing: border-box; }
  html, body { width: 902px; height: 1200px; overflow: hidden; }
  body { background: var(--page); font-family: "Lato", sans-serif; position: relative; }

  .card { position: absolute; left: 55px; width: 792px; height: 432px; background: var(--white); overflow: hidden; box-shadow: 0 4px 14px rgba(0,0,0,.18); }
  .card--front { top: 80px; }
  .card--back { top: 600px; }

  .photo { position: absolute; }
  .photo--calculator { left: 0; top: 0; width: 192px; height: 148px; background: linear-gradient(135deg, #e9e2d6, #a9b59a 60%, #6f7d5f); }
  .photo--money-stack { left: 0; top: 150px; width: 192px; height: 155px; background: linear-gradient(160deg, #ffffff, #d8ddd0 55%, #98a38c); }
  .photo--chart-team { left: 0; top: 307px; width: 192px; height: 125px; background: linear-gradient(120deg, #dfe6ee, #b9c5d3 50%, #c99a73); }
  .photo--office-team { right: 0; top: 190px; width: 230px; height: 172px; background: linear-gradient(90deg, rgba(255,255,255,1) 0%, #cfd5dc 35%, #5a5f68 75%, #c9cdd3); }

  .headline-block { position: absolute; left: 192px; top: 0; width: 391px; height: 122px; background: var(--navy); padding: 14px 0 0 14px; }
  .headline { font-family: "Bebas Neue", sans-serif; font-weight: 400; color: var(--white); text-transform: uppercase; line-height: 1; white-space: nowrap; }
  .headline__small { display: block; font-size: 44px; letter-spacing: .2px; }
  .headline__large { display: block; font-size: 56px; margin-top: 2px; }

  .brand { position: absolute; left: 583px; top: 0; width: 209px; height: 122px; display: flex; align-items: center; justify-content: center; gap: 8px; }
  .brand__mark { width: 12px; height: 12px; background: var(--green); flex: none; }
  .brand__name { font-family: "Lato", sans-serif; font-weight: 400; font-size: 16px; letter-spacing: 1px; color: var(--grey-text); text-transform: uppercase; white-space: nowrap; }

  .band { position: absolute; left: 192px; top: 122px; width: 600px; height: 68px; }
  .band svg { position: absolute; inset: 0; }
  .band__text { position: relative; padding: 8px 0 0 16px; color: var(--white); font-style: italic; font-weight: 700; font-size: 20px; line-height: 1.3; }

  .offer { position: absolute; left: 192px; top: 190px; width: 400px; padding: 8px 0 0 15px; }
  .offer__title { color: var(--navy); font-weight: 700; font-size: 16px; line-height: 1.3; margin-bottom: 10px; }
  .benefits { display: flex; gap: 6px; }
  .benefits ul { list-style: none; }
  .benefits li { position: relative; padding-left: 14px; font-style: italic; font-size: 9.4px; color: #111; margin-bottom: 7px; white-space: nowrap; }
  .benefits li::before { content: ""; position: absolute; left: 0; top: 3px; width: 6px; height: 6px; border-radius: 50%; background: var(--blue); }

  .wave { position: absolute; left: 192px; top: 325px; width: 600px; height: 38px; }

  .contact-bar { position: absolute; left: 192px; top: 362px; width: 600px; height: 70px; background: var(--navy); }
  .contact-bar svg.bar-shapes { position: absolute; inset: 0; }
  .contact-web { position: absolute; left: 60px; top: 10px; color: var(--white); font-style: italic; font-weight: 700; font-size: 11.5px; line-height: 1.45; }
  .contact-call__label { position: absolute; left: 310px; top: 8px; color: var(--white); font-weight: 700; font-size: 11.5px; line-height: 1.2; white-space: nowrap; }
  .contact-call__number { position: absolute; left: 310px; top: 26px; display: flex; align-items: center; gap: 6px; color: var(--white); font-weight: 700; font-size: 26px; line-height: 1.1; white-space: nowrap; }
  .contact-call__number svg { flex: none; }

  .back-brand { position: absolute; left: 65px; top: 60px; display: flex; align-items: center; gap: 8px; }
  .back-address { position: absolute; left: 65px; top: 92px; font-size: 10px; color: var(--grey-text); line-height: 1.25; }
  .back-tagline { position: absolute; left: 65px; top: 152px; font-weight: 700; font-size: 14px; color: var(--grey-text); line-height: 1.3; }
  .back-message { position: absolute; left: 65px; top: 208px; width: 320px; font-weight: 700; font-size: 14px; color: var(--grey-text); line-height: 1.3; }
  .stamp-box { position: absolute; left: 655px; top: 32px; width: 97px; height: 90px; border: 1px solid #cfcfcf; }
</style>
</head>
<body>

<section class="card card--front" aria-label="Mailer front">
  <div class="photo photo--calculator" role="img" aria-label="Photo of hands using a calculator over cash"></div>
  <div class="photo photo--money-stack" role="img" aria-label="Photo of stacked banknotes with a rising gold arrow"></div>
  <div class="photo photo--chart-team" role="img" aria-label="Photo of two business people pointing at a rising chart"></div>

  <div class="headline-block">
    <h1 class="headline">
      <span class="headline__small">Helping Business Focus</span>
      <span class="headline__large">On What Metters!</span>
    </h1>
  </div>

  <div class="brand">
    <span class="brand__mark"></span>
    <span class="brand__name">Tillbrook Partners</span>
  </div>

  <div class="band">
    <svg width="600" height="68" viewBox="0 0 600 68" aria-hidden="true">
      <rect width="600" height="68" fill="var(--green)"/>
      <polygon points="470,68 600,0 600,68" fill="var(--green-dark)"/>
      <polygon points="380,68 520,10 560,68" fill="#5fa634"/>
    </svg>
    <p class="band__text">We understand the merchant cash advance loans<br>can be a burden on your business</p>
  </div>

  <div class="photo photo--office-team" role="img" aria-label="Photo of two colleagues smiling at a computer in an office"></div>

  <div class="offer">
    <h2 class="offer__title">Overwhelmed by daily/weekly payments?<br>We can help!</h2>
    <div class="benefits">
      <ul>
        <li>This is not a loan, WE ARE NOT LENDERS!</li>
        <li>Improve your business cash flow immedietely</li>
        <li>Move payments to one monthly amount</li>
        <li>Reduce the amount you are paying out monthly</li>
        <li>Stretegic alternatives to high interest loans</li>
      </ul>
      <ul>
        <li>Fast, confidential business debt relief</li>
        <li>No-obligation consultation</li>
        <li>Adsolutely no credit pulls</li>
        <li>No collateral, no financials</li>
      </ul>
    </div>
  </div>

  <svg class="wave" viewBox="0 0 600 38" aria-hidden="true">
    <polygon points="0,38 0,30 200,12 330,0 420,20 600,14 600,38" fill="var(--green)"/>
    <polygon points="0,38 160,22 330,8 440,26 600,22 600,38" fill="var(--green-dark)"/>
  </svg>

  <div class="contact-bar">
    <svg class="bar-shapes" width="600" height="70" viewBox="0 0 600 70" aria-hidden="true">
      <polygon points="0,0 50,0 0,45" fill="var(--blue)"/>
      <polygon points="0,70 30,40 45,70" fill="var(--blue)"/>
      <polygon points="600,20 600,70 560,70" fill="var(--blue)"/>
      <polygon points="575,0 600,0 600,15" fill="var(--blue)"/>
    </svg>
    <p class="contact-web">Visit Our website : www.tillbrookhelp.com<br>Email : info@tillbrookhelp.com</p>
    <p class="contact-call__label">Call Now For Free Consultation With Our Experts</p>
    <p class="contact-call__number">
      <svg width="22" height="22" viewBox="0 0 24 24" aria-hidden="true">
        <circle cx="12" cy="12" r="10" fill="none" stroke="#fff" stroke-width="2"/>
        <path d="M8 7c1 0 1.5 2 1 3l-1 1c.8 1.6 2 2.8 3.5 3.5l1-1c1-.5 3 0 3 1 0 1.5-1 2.5-2.5 2.5C9 17 7 12 7 9c0-1 .3-2 1-2z" fill="#fff"/>
      </svg>
      844-555-0182
    </p>
  </div>
</section>

<section class="card card--back" aria-label="Mailer back">
  <div class="back-brand">
    <span class="brand__mark"></span>
    <span class="brand__name">Tillbrook Partners</span>
  </div>
  <p class="back-address">1450 W Maple Ave<br>Ridgefield, Harlow County 76118<br>USA</p>
  <p class="back-tagline">Stretegic Debt Relife For<br>Business of All Sizes</p>
  <p class="back-message">Stop taking out loans to pey off other loans. Take back your business cash flow, and focus on what matters.</p>
  <div class="stamp-box" aria-label="Postage area"></div>
</section>

</body>
</html>
```